Brantley Studios photography and video creator

I need a business card for my production company. I shoot photography and videography for real estate, adventure sports and businesses

Contact Information for Business Card

simple not to busy

Colors

Designer to choose colors to be used in the design.

Requirements
Must have
• derek@brantleystudios.ca
• phone -5873304127
• instagram derek_brantley

```html
<!DOCTYPE html>
<html lang="en">
<head>
<meta charset="utf-8">
<title>Brantley Studios — Business Card</title>
<link href="https://fonts.googleapis.com/css2?family=Montserrat:wght@400;700;800&display=swap" rel="stylesheet">
<style>
  :root {
    --page-bg: #1d1d1d;
    --card-black: #0c0c0c;
    --sky-white: #ffffff;
    --ridge-light: #c9c9c9;
    --ridge-mid: #7a7a7a;
    --ridge-dark: #2a2a2a;
    --text-white: #ffffff;
    --text-muted: #8a8a8a;
  }
  * { margin: 0; padding: 0; box-sizing: border-box; }
  html, body {
    width: 1200px;
    height: 900px;
    overflow: hidden;
    background: var(--page-bg);
    font-family: "Montserrat", sans-serif;
  }
  .card {
    position: absolute;
    left: 100px;
    top: 170px;
    width: 1000px;
    height: 560px;
    background: var(--card-black);
    overflow: hidden;
  }
  .card__landscape {
    position: absolute;
    inset: 0;
    background: linear-gradient(172deg,
      var(--sky-white) 0%,
      var(--sky-white) 22%,
      var(--ridge-light) 34%,
      var(--ridge-mid) 44%,
      var(--ridge-dark) 56%,
      var(--card-black) 74%);
  }
  .card__brand {
    position: absolute;
    left: 70px;
    top: 330px;
    color: var(--text-white);
    font-weight: 800;
    font-size: 44px;
    letter-spacing: 1px;
    text-transform: uppercase;
  }
  .card__contact {
    position: absolute;
    right: 60px;
    top: 270px;
    text-align: right;
    color: var(--text-muted);
    font-size: 17px;
    line-height: 1.9;
  }
  .contact-line {
    display: flex;
    justify-content: flex-end;
    align-items: center;
    gap: 8px;
  }
  .contact-line svg { width: 16px; height: 16px; flex: none; }
  .social-dot {
    width: 14px; height: 14px;
    border-radius: 50%;
    background: var(--text-muted);
    display: inline-block;
  }
  .card__tagline {
    color: var(--text-white);
    font-weight: 700;
    font-size: 17px;
    letter-spacing: 0.3px;
    margin-top: 4px;
  }
</style>
</head>
<body>
  <div class="card">
    <div class="card__landscape" role="img" aria-label="Layered grey mountain ridges with pine trees under a white sky"></div>

    <div class="card__brand">Brantley Studios</div>

    <div class="card__contact">
      <div class="contact-line">
        <span>derek_brantley</span>
        <span class="social-dot" aria-hidden="true"></span>
        <span>5873304127</span>
        <svg viewBox="0 0 16 16" aria-hidden="true">
          <path fill="#8a8a8a" d="M3.6 1.5l2.2 2.6-1.2 1.6c.9 2 2.4 3.5 4.4 4.4l1.6-1.2 2.6 2.2-1.3 2.2C6.8 13.1 2.9 9.2 1.4 3.1z"/>
        </svg>
      </div>
      <div class="contact-line">
        <span>derek@brantleystudios.ca</span>
        <svg viewBox="0 0 16 16" aria-hidden="true">
          <rect x="1.5" y="3.5" width="13" height="9" fill="none" stroke="#8a8a8a" stroke-width="1.4"/>
          <path d="M1.5 3.5l6.5 5 6.5-5" fill="none" stroke="#8a8a8a" stroke-width="1.4"/>
        </svg>
      </div>
      <div class="card__tagline">PHOTOGRAPHY &amp; VIDEOGRAPHY</div>
    </div>
  </div>
</body>
</html>
```